Supplement Bottle Label Greens Revised

We want to design a front label for a health supplement bottle. The product is called Meadow Sip Chews™. This will be a new product so there is no current website for the product. However it will be bundled with the product attached Belly Poise.
We want it to be modern, vibrant and appealing.
Bottle size: standard size supplement CLEAR bottle size, with white child resistant cap and the label panel dimensions are 3” x 7”. The label should be primarily white and green, with a touch of red; (see color palettes)/it can also ONLY be white and green. It should complement the Belly Poise bottle when it’s right next to it.
We are only focused on the front of the bottle design, not on the back, but leave space for the supplement panel and other text on the back.
So the text for the front of the bottle is:
RW Talbot's
Meadow Sip Chews™
Super Greens Blend for:
Energy, Digestion, and Immune Support*
60 Gummies | Dietary Supplement
Raspberry Flavor Gummies
Off to side of the label:
Non-GMO
Vegan Friendly
Plant-Based
Gelatin Free

```html
<!DOCTYPE html>
<html lang="en">
<head>
<meta charset="utf-8">
<title>Meadow Sip Chews™ Label</title>
<link href="https://fonts.googleapis.com/css2?family=Josefin+Sans:wght@400;600;700&display=swap" rel="stylesheet">
<style>
  :root {
    --bg: #ececec;
    --white: #ffffff;
    --green-deep: #1f7a3a;
    --green-title: #2f8f3f;
    --green-panel: #59a23f;
    --green-light: #8cc46a;
    --facts-fill: #eef4ea;
    --facts-line: #ffffff;
    --ink: #1d2a20;
  }
  html, body {
    margin: 0;
    padding: 0;
    width: 1200px;
    height: 2400px;
    overflow: hidden;
    background: var(--bg);
    font-family: "Josefin Sans", sans-serif;
  }
  .canvas {
    position: relative;
    width: 1200px;
    height: 2400px;
  }
  .label {
    position: absolute;
    left: 0;
    top: 943px;
    width: 1200px;
    height: 514px;
    background: var(--white);
    overflow: hidden;
  }
  .label-art {
    position: absolute;
    inset: 0;
  }
  .facts-panel {
    position: absolute;
    left: 68px;
    top: 75px;
    width: 309px;
    height: 309px;
    background: var(--facts-fill);
    border-radius: 22px;
    overflow: hidden;
  }
  .facts-title {
    margin: 0;
    padding: 16px 17px 0;
    height: 32px;
    font-size: 19px;
    font-weight: 400;
    letter-spacing: 0.5px;
    color: var(--green-deep);
    border-bottom: 2px solid var(--facts-line);
  }
  .facts-row {
    height: 42px;
    border-bottom: 2px solid var(--facts-line);
  }
  .brand-name {
    position: absolute;
    left: 390px;
    width: 400px;
    top: 70px;
    text-align: center;
    font-size: 33px;
    font-weight: 700;
    color: var(--green-deep);
  }
  .product-title {
    position: absolute;
    left: 440px;
    width: 300px;
    top: 208px;
    text-align: center;
    margin: 0;
    font-size: 27px;
    font-weight: 700;
    line-height: 32px;
    letter-spacing: 1px;
    color: var(--green-title);
  }
  .product-title .dark { color: var(--ink); }
  .count {
    position: absolute;
    left: 440px;
    width: 300px;
    top: 311px;
    text-align: center;
    color: var(--green-title);
    font-weight: 700;
  }
  .count-number { display: block; font-size: 23px; line-height: 24px; }
  .count-unit { display: block; font-size: 12px; font-weight: 600; }
  .tagline {
    position: absolute;
    left: 68px;
    top: 458px;
    margin: 0;
    font-size: 16px;
    letter-spacing: 1px;
    color: var(--green-deep);
  }
  .side-info {
    position: absolute;
    left: 858px;
    top: 120px;
    color: var(--white);
  }
  .flavor {
    margin: 0 0 20px;
    font-size: 19px;
    line-height: 22px;
    letter-spacing: 1px;
  }
  .flavor strong { font-weight: 700; }
  .claims {
    list-style: none;
    margin: 0;
    padding: 0;
  }
  .claim {
    display: flex;
    align-items: center;
    height: 69px;
    font-size: 21px;
    letter-spacing: 0.8px;
  }
  .claim svg { margin-right: 14px; flex: none; }
</style>
</head>
<body>
<main class="canvas">
  <section class="label">
    <svg class="label-art" width="1200" height="514" viewBox="0 0 1200 514">
      <defs>
        <radialGradient id="ringTone" cx="50%" cy="50%" r="50%">
          <stop offset="0.62" stop-color="#ffffff" stop-opacity="1"/>
          <stop offset="0.72" stop-color="#8cc46a" stop-opacity="0.85"/>
          <stop offset="0.88" stop-color="#2f8f3f" stop-opacity="0.95"/>
          <stop offset="1" stop-color="#1f7a3a" stop-opacity="0"/>
        </radialGradient>
      </defs>
      <path class="panel-sweep" d="M760 0 L 900 0 L 900 300 C 830 300, 760 240, 760 0 Z" fill="#8cc46a" opacity="0.45"/>
      <path class="panel-green" d="M835 0 C 755 110, 745 380, 780 514 L1200 514 L1200 0 Z" fill="#59a23f"/>
      <g role="img" aria-label="Green liquid splash swirling around the product name">
        <circle cx="590" cy="273" r="175" fill="url(#ringTone)"/>
      </g>
    </svg>

    <div class="facts-panel">
      <h3 class="facts-title">SUPPLEMENT FACTS</h3>
      <div class="facts-row"></div>
      <div class="facts-row"></div>
      <div class="facts-row"></div>
      <div class="facts-row"></div>
      <div class="facts-row"></div>
    </div>

    <div class="brand-name">RW Talbot's</div>
    <h1 class="product-title">MEADOW<br>SIP<br><span class="dark">CHEWS™</span></h1>
    <div class="count"><span class="count-number">60</span><span class="count-unit">Gummies</span></div>

    <p class="tagline">SUPER GREENS BLEND FOR: ENERGY, DIGESTION, AND IMMUNE SUPPORT*</p>

    <div class="side-info">
      <p class="flavor">RASPBERRY FLAVOR GUMMIES<br><strong>DIETARY SUPPLEMENT</strong></p>
      <ul class="claims">
        <li class="claim">
          <svg width="56" height="56" viewBox="0 0 56 56"><circle cx="28" cy="28" r="26" fill="none" stroke="#fff" stroke-width="2"/><circle cx="28" cy="28" r="19" fill="none" stroke="#fff" stroke-width="2"/><path d="M21 18 C 35 24, 21 32, 35 38 M35 18 C 21 24, 35 32, 21 38" fill="none" stroke="#fff" stroke-width="2"/><path d="M24 21 H32 M24 35 H32 M26 28 H30" stroke="#fff" stroke-width="1.5"/></svg>
          NON-GMO
        </li>
        <li class="claim">
          <svg width="56" height="56" viewBox="0 0 56 56"><circle cx="28" cy="28" r="26" fill="none" stroke="#fff" stroke-width="2"/><circle cx="28" cy="28" r="19" fill="none" stroke="#fff" stroke-width="2"/><path d="M20 30 C 22 20, 32 18, 37 20 C 36 30, 28 36, 20 30 Z" fill="#fff"/></svg>
          VEGAN FRIENDLY
        </li>
        <li class="claim">
          <svg width="56" height="56" viewBox="0 0 56 56"><circle cx="28" cy="28" r="26" fill="none" stroke="#fff" stroke-width="2"/><circle cx="28" cy="28" r="19" fill="none" stroke="#fff" stroke-width="2"/><path d="M28 38 V22 M28 30 C 22 28, 20 24, 21 21 C 25 21, 28 24, 28 28 M28 27 C 34 25, 36 21, 35 18 C 31 18, 28 21, 28 25" fill="none" stroke="#fff" stroke-width="2"/></svg>
          PLANT-BASED
        </li>
        <li class="claim">
          <svg width="56" height="56" viewBox="0 0 56 56"><circle cx="28" cy="28" r="26" fill="none" stroke="#fff" stroke-width="2"/><circle cx="28" cy="28" r="19" fill="none" stroke="#fff" stroke-width="2"/><path d="M21 35 L35 21" stroke="#fff" stroke-width="5" stroke-linecap="round"/><circle cx="20" cy="33" r="3" fill="#fff"/><circle cx="23" cy="36" r="3" fill="#fff"/><circle cx="33" cy="20" r="3" fill="#fff"/><circle cx="36" cy="23" r="3" fill="#fff"/></svg>
          GELATIN FREE
        </li>
      </ul>
    </div>
  </section>
</main>
</body>
</html>
```